Valmira Engineering Pty Ltd - designed for architects to look at products

We need a web design which is modern and stands out. Our company will distribute electronic drives to Australia and New Zealand. The company is called Valmira Engineering. This website will be looked at by architects and manufacturers that will use or specify this product in the healthcare industry, automotive industry and food processing industry. Our product is designed to automate things such as wheelchairs, windows, hospital beds ect. We get our product from the manufacturer in Denmark called 'Brulvak'.
I need someone to take all the information and the logo from their website but change the way it is set up and the colours. We dont want to use their contact information.
www.brulvak.example
Pictures must be used too.
Contact information below;

Valmira Engineering PTY LTD
ACN (Australian Company Number): 248 613 507
Postal Address: PO Box 4817, Kelbrook Flats, Western Australia 6099
hugo@valmira.example.au
neil@valmira.example.au

Phone Fax
0291846502 0291846513 Sydney

0374518830 0374518831 Melbourne

0748275106 0748275117 Brisbane

0861947720 0861947731 Adelaide

0874639204 0874639205 Perth

038265703 038265704 Christchurch

094670315 094670316 Auckland

Target Market(s)

Architects, engineers and manufacturers

Industry/Entity Type

Automotive

Requirements
Must have
• Please include all case studies with photos from the brulvak website www.brulvak.example.au
I do not want this website looking anything like theirs please
Should not have
• No links to facebook, twitter or any other sites like that

```html
<!DOCTYPE html>
<html lang="en">
<head>
<meta charset="utf-8">
<title>Valmira Engineering</title>
<link rel="stylesheet" href="https://fonts.googleapis.com/css2?family=Open+Sans:wght@300;400;600;700&family=Arimo:wght@400;700&display=swap">
<style>
:root{
  --navy:#0b4d86;
  --blue:#0d5d9f;
  --bright:#1a8be0;
  --btn:#0a4f8c;
  --ink:#2b2b2b;
  --grey:#555;
  --line:#dcdcdc;
  --panel:#f5f5f5;
  --page:#f9f9f9;
}
*{box-sizing:border-box;margin:0;padding:0}
html,body{width:1070px;height:1200px;overflow:hidden}
body{position:relative;background:var(--page);font-family:"Arimo",Arial,sans-serif;color:var(--ink)}
.abs{position:absolute}

.topbar{left:0;top:0;width:1070px;height:38px;background:var(--navy)}
.tabs{left:34px;top:8px;width:400px;height:30px;list-style:none;font-family:"Open Sans",sans-serif;font-size:13px}
.tabs li{position:absolute;top:0;height:30px;line-height:32px;color:#fff}
.tabs li.active{left:0;width:72px;text-align:center;background:linear-gradient(#fff,#e9e9e9);color:#666;border-radius:8px 8px 0 0}

.header{left:26px;top:38px;width:998px;height:125px;background:linear-gradient(#fdfdfd,#ececec);box-shadow:0 3px 5px rgba(0,0,0,.18)}
.brand{left:12px;top:34px;display:flex;align-items:center;gap:10px}
.brand-name{font-family:"Open Sans",sans-serif;font-size:26px;font-weight:400;color:var(--blue);letter-spacing:.3px}
.brand-dot{width:26px;height:26px;border-radius:50%;background:var(--blue)}
.tagline{left:42px;top:76px;font-size:15px;color:#444;letter-spacing:.5px}
.search-label{left:707px;top:14px;font-family:"Open Sans",sans-serif;font-size:13px;font-weight:600;color:#666}
.search-box{left:782px;top:9px;width:184px;height:26px;border:1px solid #ccc;border-radius:13px 0 0 13px;background:#f4f4f4;font-size:11px;color:#aaa;line-height:24px;padding-left:8px}
.search-btn{left:964px;top:9px;width:28px;height:26px;background:#2d5fa3}

.hero{left:31px;top:183px;width:980px;height:325px;border:1px solid var(--line);background:#fff}
.hero-img{left:9px;top:8px;width:962px;height:307px;background:linear-gradient(#3a3a3a 0%,#6b6b6b 35%,#4d3b33 70%,#2a2624 100%)}
.hero-text{left:11px;top:10px;font-family:"Open Sans",sans-serif;font-weight:300;font-size:24px;line-height:31px;color:#fff}
.hero-text strong{font-weight:700;color:var(--bright)}

.about{left:34px;top:527px;width:658px;height:236px;background:var(--panel);border:1px solid var(--line);border-radius:10px}
.about h2{position:absolute;left:6px;top:4px;font-family:"Open Sans",sans-serif;font-weight:400;font-size:19px;color:#666;border-bottom:1px dotted #999;padding-bottom:1px}
.about h2 span{color:var(--blue);font-weight:600;font-variant:small-caps;font-size:21px}
.about p{position:absolute;left:6px;width:632px;font-size:11.5px;line-height:20px;color:#333;text-align:justify;letter-spacing:.3px}

.btn{display:block;background:var(--btn);color:#fff;font-size:11px;border-radius:4px;height:23px;line-height:23px;padding:0 7px;box-shadow:0 1px 2px rgba(0,0,0,.3)}

.contact{left:705px;top:530px;width:304px;height:207px;border-radius:10px;background:linear-gradient(#0b74c8,#0a5aa3 50%,#033b74);color:#fff;box-shadow:0 10px 10px -4px rgba(0,0,0,.25)}
.contact h2{position:absolute;left:14px;top:20px;font-family:"Open Sans",sans-serif;font-weight:400;font-size:23px}
.contact address{position:absolute;left:15px;top:56px;font-style:normal;font-size:12px;line-height:18px;letter-spacing:.2px}
.contact address b{font-weight:700}
.note-art{left:222px;top:0px;width:106px;height:92px;border-radius:6px;background:linear-gradient(135deg,#eef3f8,#c7d6e4)}

.band{left:0;top:776px;width:1070px;height:302px;border-top:2px solid #e2e2e2;background:#fafafa}
.card{width:261px;height:275px;background:#f8f8f8;border:2px solid #e0e0e0;border-top:none;box-shadow:0 12px 10px -6px rgba(0,0,0,.2);top:0}
.card-head{position:absolute;left:26px;top:10px;display:flex;align-items:center}
.card-dot{width:36px;height:36px;border-radius:50%;background:var(--blue);position:relative;z-index:1}
.card-pill{height:35px;line-height:35px;padding:0 10px;margin-left:-4px;border-radius:0 18px 18px 0;background:linear-gradient(#f4f4f4,#d4d4d4);font-family:"Open Sans",sans-serif;font-size:16px;color:#444}
.card-photo{position:absolute;left:11px;top:56px;width:236px;height:104px;border:1px solid #ddd;background:#fff;padding:3px}
.card-photo div{width:100%;height:100%}
.photo-site{background:linear-gradient(#d8c64a,#8f8f86 45%,#6b6660)}
.photo-steel{background:linear-gradient(#c9cccf,#8a8e92 55%,#2b2d30)}
.card p{position:absolute;left:14px;top:168px;width:230px;font-size:11.5px;line-height:18px;text-align:justify;color:#333;letter-spacing:.2px}
.card .btn{position:absolute;right:13px;bottom:8px}

.footer{left:0;top:1080px;width:1070px;height:120px;border-top:2px solid #e0e0e0;background:linear-gradient(#fff,#e6e6e6)}
.foot-col{top:22px;font-size:13px}
.foot-col h3{font-size:13px;font-weight:700;color:#333;margin-bottom:4px}
.foot-col ul{list-style:none;font-size:11.5px;color:#444;line-height:18px;padding-left:4px}
.foot-col li::before{content:"";display:inline-block;width:6px;height:6px;border-radius:50%;background:var(--blue);margin-right:10px;vertical-align:1px}
.foot-nav{right:68px;top:18px;font-size:12px;color:#555;letter-spacing:.4px;word-spacing:2px}
.foot-nav span{margin:0 26px}
.foot-brand{right:68px;top:42px;font-family:"Open Sans",sans-serif;font-weight:400;font-size:24px;color:var(--blue)}
.foot-tag{right:68px;top:76px;font-size:13px;color:#444;letter-spacing:.4px}
</style>
</head>
<body>

<div class="abs topbar">
  <ul class="abs tabs">
    <li class="active">Home</li>
    <li style="left:104px">Search</li>
    <li style="left:199px">Contact</li>
    <li style="left:301px">Brulvak</li>
  </ul>
</div>

<header class="abs header">
  <div class="abs brand"><span class="brand-name">Valmira Engineering</span><span class="brand-dot"></span></div>
  <div class="abs tagline">- excellent electric actuators</div>
  <div class="abs search-label">Search for:</div>
  <div class="abs search-box">-----Search here--------------</div>
  <div class="abs search-btn">
    <svg width="28" height="26" viewBox="0 0 28 26"><circle cx="12" cy="11" r="5.5" fill="none" stroke="#fff" stroke-width="2.2"/><line x1="16" y1="15" x2="21" y2="20" stroke="#fff" stroke-width="3" stroke-linecap="round"/></svg>
  </div>
</header>

<section class="abs hero">
  <div class="abs hero-img" role="img" aria-label="Dramatic photograph of an industrial steel works with pipes and towers under a stormy sky">
    <div class="abs hero-text"><strong>ACTUATORS IN STAINLESS</strong> Steel With IP68<br>or IP69K Protection Class Go to<br>Product Selection....</div>
  </div>
</section>

<section class="abs about">
  <h2>ABOUT <span>Valmira Engineering</span></h2>
  <p style="top:41px"><b>Lorem Ipsum is simply dummy text of the printing and typesetting industry. Lorem Ipsum has been the industry's standard dummy text</b> ever since the 1500s, when an unknown printer took a galley of type and scrambled it to make a type specimen book. It has survived not only five centuries, but also the leap into electronic typesetting, remaining essentially unchanged.</p>
  <p style="top:141px">It was popularised in the 1960s with the release of Pressfont sheets containing Lorem Ipsum passages, and more recently with desktop publishing software like Orvel PageSetter including versions of Lorem Ipsum.</p>
  <a class="abs btn" style="left:560px;top:203px">Read more ›</a>
</section>

<aside class="abs contact">
  <div class="abs note-art" role="img" aria-label="Illustration of a note pad with a fountain pen"></div>
  <h2>Contact us!</h2>
  <address>
    <b>Valmira Engineering PTY LTD</b><br>
    ACN (Australian Company Number)<br>
    : 248 613 507 Postal Address:<br>
    PO Box 4817, Kelbrook Flats,<br>
    Western Australia 6099<br>
    hugo@valmira.example.au<br>
    neil@valmira.example.au<br>
    Phone Fax 0291846502 0291846513 Sydney
  </address>
</aside>

<section class="abs band">
  <article class="abs card" style="left:83px">
    <div class="card-head"><span class="card-dot"></span><span class="card-pill" style="width:154px">Industrial</span></div>
    <div class="card-photo"><div class="photo-site" role="img" aria-label="Photograph of a worker on a steel fabrication site under yellow gantry cranes"></div></div>
    <p><b>Lorem Ipsum is simply dummy text of the printing and</b> typesetting industry. Lorem Ipsum has been the industry's standard dummy text.</p>
    <a class="btn">Read more ›</a>
  </article>
  <article class="abs card" style="left:400px">
    <div class="card-head" style="left:17px"><span class="card-dot"></span><span class="card-pill" style="width:206px;padding-left:18px">Stainless Steel</span></div>
    <div class="card-photo"><div class="photo-steel" role="img" aria-label="Photograph of stacked stainless steel tubes"></div></div>
    <p style="top:172px"><b>Lorem Ipsum is simply dummy text of the printing and</b> typesetting industry. Lorem Ipsum has been the industry's standard dummy text.</p>
    <a class="btn">Read more ›</a>
  </article>
  <article class="abs card" style="left:723px">
    <div class="card-head" style="left:20px"><span class="card-dot"></span><span class="card-pill" style="width:196px">Rehab, Medical &amp; Care</span></div>
    <div class="card-photo"><div class="photo-site" role="img" aria-label="Photograph of a worker on a steel fabrication site under yellow gantry cranes"></div></div>
    <p style="top:165px"><b>Lorem Ipsum is simply dummy text of the printing and</b> typesetting industry. Lorem Ipsum has been the industry's standard dummy text.</p>
    <a class="btn">Read more ›</a>
  </article>
</section>

<footer class="abs footer">
  <div class="abs foot-col" style="left:39px"><h3>Actuators</h3><ul><li>vx35</li><li>vx50</li></ul></div>
  <div class="abs foot-col" style="left:168px"><h3>Basic Controllers</h3><ul><li>K2-04</li><li>K2-15</li></ul></div>
  <div class="abs foot-col" style="left:337px"><h3>Basic Controllers</h3><ul><li>K2-20</li><li>K3</li></ul></div>
  <nav class="abs foot-nav">Home<span>|</span>Search<span>|</span>Contact<span>|</span>Brulvak</nav>
  <div class="abs foot-brand">Brulvak</div>
  <div class="abs foot-tag">- excellent electric actuators</div>
</footer>

</body>
</html>
```